App Design

This is a 'video player' app - will be used to stream video files and watch them on a device. Need 3/4 skins for user customization.
Design will need to be versatile - used on: Veltrax4/4S/5 and zorBex2/3
Require an app design that shows the required functionality described by us, allows ease to navigate and visually creates a unique user experience.
App must have following pages: (refer to attached pages)
1. Search Page
2. Results Page
3. Video Page
4. End Page
3-4 skins for user preference
important: if you are interested please submit designs by tomorrow night - we will be picking from submitted designs - will make revisions and finalize the design within 4-5 days.
timing is crucial- please only submit if you can commit to timeline and design requirements. There will be refinements required.
Please see the attached update.
Additional reference files have been added to help in your efforts.
We have added a sample design that may help with your submissions. Please see brief
Project Deadline Extended
Project Deadline Extended
Project Deadline Extended
Target Market(s)
early adapters for technology / veltrax, tablet, quillon users
Requirements
Should not have
- should not be generic design

```html
<!DOCTYPE html>
<html lang="en">
<head>
<meta charset="utf-8">
<title>Video Galleries</title>
<link href="https://fonts.googleapis.com/css2?family=Arimo:wght@400;700&family=Open+Sans:wght@400;600;700&display=swap" rel="stylesheet">
<style>
  :root {
    --page-bg: #d6a3a2;
    --status-bg: #000000;
    --nav-top: #474747;
    --nav-bottom: #242424;
    --content-bg: #e7e1d8;
    --row-bg: #f0eff0;
    --divider: #c9c2b6;
    --divider-light: #f7f3ec;
    --title-ink: #2b2b2b;
    --body-ink: #3e3e3e;
    --white: #ffffff;
    --ribbon: #c8262d;
    --ribbon-dark: #8f151b;
    --tab-dark: #1c1e22;
  }
  * { margin: 0; padding: 0; box-sizing: border-box; }
  html, body { width: 1200px; height: 928px; overflow: hidden; }
  body { background: var(--page-bg); position: relative; }

  .app-screen {
    position: absolute;
    left: 306px; top: 30px;
    width: 368px; height: 542px;
    transform: scale(1.6);
    transform-origin: top left;
    background: var(--content-bg);
    overflow: hidden;
    font-family: "Open Sans", sans-serif;
  }

  .status-bar {
    position: absolute; left: 0; top: 0; width: 368px; height: 18px;
    background: var(--status-bg); color: var(--white);
    font-family: "Arimo", sans-serif; font-size: 12px;
  }
  .status-bar .signal { position: absolute; left: 5px; top: 3px; }
  .status-bar .carrier { position: absolute; left: 29px; top: 1px; }
  .status-bar .wifi { position: absolute; left: 72px; top: 2px; }
  .status-bar .clock { position: absolute; left: 0; right: 0; top: 1px; text-align: center; }
  .status-bar .battery { position: absolute; right: 5px; top: 4px; }

  .nav-bar {
    position: absolute; left: 0; top: 18px; width: 368px; height: 52px;
    background: linear-gradient(var(--nav-top), var(--nav-bottom));
    border-bottom: 1px solid #111;
  }
  .back-button {
    position: absolute; left: 8px; top: 9px; width: 64px; height: 34px;
  }
  .back-button span {
    position: absolute; left: 18px; top: 8px;
    font-family: "Arimo", sans-serif; font-weight: 700; font-size: 15px; color: var(--white);
  }
  .nav-title {
    position: absolute; left: 100px; top: 11px;
    font-family: "Arimo", sans-serif; font-weight: 700; font-size: 23px; color: var(--white);
    text-shadow: 0 -1px 0 rgba(0,0,0,.6);
  }

  .gallery-list { position: absolute; left: 8px; top: 80px; width: 350px; list-style: none; }
  .gallery-item {
    position: relative; height: 76px; margin-bottom: 19px;
    background: var(--row-bg); display: flex;
    box-shadow: 0 1px 1px rgba(0,0,0,.12);
  }
  .gallery-item::after {
    content: ""; position: absolute; left: 0; right: 0; bottom: -10px;
    height: 1px; background: var(--divider); border-bottom: 1px solid var(--divider-light);
  }
  .gallery-item:last-child::after { display: none; }
  .thumb { width: 143px; height: 76px; flex: none; }
  .thumb-dew { background: linear-gradient(135deg, #2d3b18 0%, #b8b424 40%, #7b8a2c 65%, #1c2a3a 100%); }
  .thumb-cabin { background: linear-gradient(#4f6ea6 0%, #8aa0b8 30%, #6b5234 55%, #58a02a 80%, #8ccc2c 100%); }
  .thumb-lights { background: linear-gradient(#3c4fb0 0%, #7a5ac4 40%, #e0902e 58%, #2b2a7c 75%, #1d1650 100%); }
  .thumb-field { background: linear-gradient(#6a6a70 0%, #a79aa2 22%, #c0243e 45%, #8e0f26 100%); }

  .item-text { position: relative; flex: 1; padding: 9px 24px 0 8px; }
  .item-title { font-size: 14.5px; font-weight: 700; color: var(--title-ink); white-space: nowrap; }
  .item-desc { margin-top: 6px; font-size: 12px; line-height: 14px; color: var(--body-ink); }
  .chevron { position: absolute; right: 9px; top: 33px; }

  .featured-ribbon { position: absolute; left: 114px; top: -3px; }

  .tab-bar { position: absolute; left: 0; top: 490px; width: 368px; height: 52px; }
</style>
</head>
<body>
  <main class="app-screen">
    <header class="status-bar">
      <svg class="signal" width="20" height="11" viewBox="0 0 20 11" aria-hidden="true">
        <rect x="0" y="8" width="3" height="3" fill="#fff"/>
        <rect x="4" y="6" width="3" height="5" fill="#fff"/>
        <rect x="8" y="4" width="3" height="7" fill="#fff"/>
        <rect x="12" y="2" width="3" height="9" fill="#fff"/>
        <rect x="16" y="0" width="3" height="11" fill="#fff"/>
      </svg>
      <span class="carrier">Kelvo</span>
      <svg class="wifi" width="18" height="13" viewBox="0 0 18 13" aria-hidden="true">
        <path d="M1 5a11 11 0 0 1 16 0" stroke="#fff" stroke-width="2" fill="none"/>
        <path d="M4 8a7 7 0 0 1 10 0" stroke="#fff" stroke-width="2" fill="none"/>
        <circle cx="9" cy="11" r="1.8" fill="#fff"/>
      </svg>
      <span class="clock">12:34 PM</span>
      <svg class="battery" width="22" height="10" viewBox="0 0 22 10" aria-hidden="true">
        <rect x="0.5" y="0.5" width="19" height="9" fill="none" stroke="#fff"/>
        <rect x="2" y="2" width="16" height="6" fill="#ddd"/>
        <rect x="20" y="3" width="2" height="4" fill="#fff"/>
      </svg>
    </header>

    <nav class="nav-bar">
      <a class="back-button">
        <svg width="64" height="34" viewBox="0 0 64 34" aria-hidden="true">
          <defs>
            <linearGradient id="backFill" x1="0" y1="0" x2="0" y2="1">
              <stop offset="0" stop-color="#2e2e2e"/>
              <stop offset="1" stop-color="#151515"/>
            </linearGradient>
          </defs>
          <path d="M1 17 L13 1.5 H60 a3 3 0 0 1 3 3 V29.5 a3 3 0 0 1 -3 3 H13 Z" fill="url(#backFill)" stroke="#0a0a0a"/>
        </svg>
        <span>Back</span>
      </a>
      <h1 class="nav-title">Video Galleries</h1>
    </nav>

    <ul class="gallery-list">
      <li class="gallery-item">
        <div class="thumb thumb-dew" role="img" aria-label="Close-up photo of a yellow leaf with water drops"></div>
        <div class="item-text">
          <h2 class="item-title">Sunday Late Show</h2>
          <p class="item-desc">Lorem ipsum dolor sit amet, consectetur adipiscing elit</p>
          <svg class="chevron" width="7" height="10" viewBox="0 0 7 10" aria-hidden="true"><path d="M1 1l4 4-4 4" stroke="#222" stroke-width="2" fill="none"/></svg>
        </div>
      </li>
      <li class="gallery-item">
        <div class="thumb thumb-cabin" role="img" aria-label="Photo of a grass-roofed cabin by a lake"></div>
        <div class="item-text">
          <h2 class="item-title">Late hour with Dann...</h2>
          <p class="item-desc">Phasellus dictum ante eget urna feugiat non figuranti ...</p>
          <svg class="chevron" width="7" height="10" viewBox="0 0 7 10" aria-hidden="true"><path d="M1 1l4 4-4 4" stroke="#222" stroke-width="2" fill="none"/></svg>
        </div>
      </li>
      <li class="gallery-item">
        <div class="thumb thumb-lights" role="img" aria-label="Photo of city lights reflected on water at dusk"></div>
        <svg class="featured-ribbon" width="34" height="42" viewBox="0 0 34 42" aria-label="Featured" role="img">
          <path d="M0 3 H3 V0 Z" fill="var(--ribbon-dark)"/>
          <path d="M3 0 H34 V38 L18.5 32 L3 38 Z" fill="var(--ribbon)"/>
          <path d="M18.5 10 l2.4 5 5.4.6 -4 3.7 1.1 5.3 -4.9-2.7 -4.9 2.7 1.1-5.3 -4-3.7 5.4-.6z" fill="#fff"/>
        </svg>
        <div class="item-text">
          <h2 class="item-title">Nation's got flair</h2>
          <p class="item-desc">Lorem ipsum dolor sit amet, consectetur adipiscing elit.</p>
          <svg class="chevron" width="7" height="10" viewBox="0 0 7 10" aria-hidden="true"><path d="M1 1l4 4-4 4" stroke="#222" stroke-width="2" fill="none"/></svg>
        </div>
      </li>
      <li class="gallery-item">
        <div class="thumb thumb-field" role="img" aria-label="Photo of a field of red tulips"></div>
        <div class="item-text">
          <h2 class="item-title">Late hour with Dann...</h2>
          <p class="item-desc">Lorem ipsum dolor sit amet, consectetur adipiscing elit...</p>
          <svg class="chevron" width="7" height="10" viewBox="0 0 7 10" aria-hidden="true"><path d="M1 1l4 4-4 4" stroke="#222" stroke-width="2" fill="none"/></svg>
        </div>
      </li>
    </ul>

    <svg class="tab-bar" viewBox="0 0 368 52" aria-label="View switcher: list and grid" role="img">
      <path d="M0 52 V40 H80 C104 40 104 10 130 10 H238 C264 10 264 40 288 40 H368 V52 Z" fill="var(--tab-dark)"/>
      <g fill="#fff">
        <rect x="136" y="19" width="32" height="4" rx="1"/>
        <rect x="136" y="26" width="32" height="4" rx="1"/>
        <rect x="136" y="33" width="32" height="4" rx="1"/>
      </g>
      <g fill="#fff">
        <rect x="202" y="14" width="7" height="7"/><rect x="211" y="14" width="7" height="7"/><rect x="220" y="14" width="7" height="7"/>
        <rect x="202" y="23" width="7" height="7"/><rect x="211" y="23" width="7" height="7"/><rect x="220" y="23" width="7" height="7"/>
        <rect x="202" y="32" width="7" height="7"/><rect x="211" y="32" width="7" height="7"/><rect x="220" y="32" width="7" height="7"/>
      </g>
    </svg>
  </main>
</body>
</html>
```